Quick Banner Ad Job for IT Services Company

Need a collection of banner ads based around a common theme and message.

Main Theme.

IT Support and Managed Services - IT support you can rely on.
Free remote monitoring and alerting*
*conditions apply <-- this in small text

Secondary Content

Our customers are attracted by our exceptional level of customer service and trust us in providing them with support and advice over a long term relationship.

Note:
* Logos and colours attached. Only use these colours.
* Font is to be Myriad Pro

* Delivery will require the following sizes.
Leaderboard: 728×90
Medium Rectangle: 300×250
Wide Skyscraper: 160×600

Do the initial draft in leaderboard, other sizes can be worked once we have an agreed design for the main

Final delivery will also need to be in an editable format, not just final images.

Industry/Entity Type

It Company

```html
<!DOCTYPE html>
<html lang="en">
<head>
<meta charset="utf-8">
<title>ByteHarbor – IT Support Banner Set</title>
<link href="https://fonts.googleapis.com/css2?family=Source+Sans+3:ital,wght@0,400;0,600;0,700;1,400&display=swap" rel="stylesheet">
<style>
  :root {
    --cyan: #16b2e8;
    --cyan-deep: #0e86c2;
    --navy: #0a3b5a;
    --navy-dark: #08283d;
    --ink: #0a0f14;
    --white: #ffffff;
    --stage: #e9e6e1;
  }
  * { margin: 0; padding: 0; box-sizing: border-box; }
  html, body { width: 1200px; height: 1200px; overflow: hidden; }
  body {
    background: var(--stage);
    font-family: "Source Sans 3", "Myriad Pro", sans-serif;
    position: relative;
  }
  .banner { position: absolute; overflow: hidden; background: var(--white); box-shadow: 0 2px 8px rgba(0,0,0,.15); }
  .banner svg.bg { position: absolute; inset: 0; }
  .banner .txt { position: absolute; white-space: nowrap; }
  .brand {
    position: absolute; display: flex; flex-direction: column; align-items: center;
    color: var(--navy); font-weight: 700; white-space: nowrap; line-height: 1;
  }
  .brand .dot { border-radius: 50%; background: var(--cyan); display: block; }

  /* Leaderboard */
  .leaderboard { left: 92px; top: 104px; width: 1032px; height: 126px; }
  .leaderboard .brand { left: 8px; width: 130px; top: 28px; gap: 8px; font-size: 21px; }
  .leaderboard .brand .dot { width: 28px; height: 28px; }
  .leaderboard .headline { left: 196px; width: 400px; text-align: center; font-weight: 700; font-size: 27px; color: var(--ink); line-height: 36px; }
  .leaderboard .offer { left: 196px; width: 400px; top: 84px; text-align: center; font-style: italic; font-size: 25px; color: var(--white); line-height: 36px; }
  .leaderboard .blurb { right: 74px; top: 16px; text-align: right; font-style: italic; font-size: 13.5px; line-height: 18.5px; color: var(--ink); }
  .leaderboard .terms { right: -30px; top: 56px; font-size: 8px; color: var(--navy-dark); transform: rotate(-90deg); }

  /* Medium rectangle */
  .rectangle { left: 188px; top: 420px; width: 612px; height: 510px; }
  .rectangle .brand { left: 446px; width: 168px; top: 30px; gap: 14px; font-size: 30px; }
  .rectangle .brand .dot { width: 46px; height: 46px; }
  .rectangle .headline { left: 44px; top: 34px; font-weight: 700; font-size: 42px; line-height: 54px; color: var(--ink); }
  .rectangle .subline { left: 44px; top: 150px; font-weight: 700; font-size: 32px; line-height: 40px; color: var(--navy); }
  .rectangle .offer { left: 0; width: 616px; top: 212px; text-align: center; font-style: italic; font-size: 35px; line-height: 45px; color: var(--white); }
  .rectangle .blurb { left: 0; width: 612px; top: 384px; text-align: center; font-size: 20.5px; line-height: 27px; color: var(--ink); }
  .rectangle .terms { right: 31px; top: 478px; font-size: 15px; color: var(--ink); }

  /* Wide skyscraper */
  .skyscraper { left: 848px; top: 256px; width: 226px; height: 852px; }
  .skyscraper .brand { left: 0; width: 226px; top: 28px; gap: 12px; font-size: 26px; }
  .skyscraper .brand .dot { width: 30px; height: 30px; }
  .skyscraper .headline { left: 0; width: 226px; top: 134px; text-align: center; font-weight: 700; font-size: 37px; line-height: 56px; color: var(--ink); }
  .skyscraper .subline { left: 0; width: 226px; top: 356px; text-align: center; font-weight: 700; font-size: 32px; line-height: 52px; color: var(--navy); }
  .skyscraper .offer { left: 0; width: 226px; top: 512px; text-align: center; font-style: italic; font-size: 30px; line-height: 41px; color: var(--white); }
  .skyscraper .blurb { left: 0; width: 226px; top: 697px; text-align: center; font-size: 15px; line-height: 19px; color: var(--ink); }
  .skyscraper .terms { left: 0; width: 226px; top: 826px; text-align: center; font-size: 11px; color: var(--ink); }
</style>
</head>
<body>

<section class="banner leaderboard" aria-label="Leaderboard banner">
  <svg class="bg" width="1032" height="126" viewBox="0 0 1032 126">
    <defs>
      <linearGradient id="lbBlue" x1="0" y1="0" x2="1" y2="0">
        <stop offset="0" stop-color="var(--cyan)"/>
        <stop offset=".6" stop-color="var(--cyan-deep)"/>
        <stop offset="1" stop-color="var(--navy)"/>
      </linearGradient>
    </defs>
    <rect width="1032" height="126" fill="url(#lbBlue)"/>
    <path d="M0 0 H136 Q156 70 96 126 H0 Z" fill="var(--white)"/>
    <path d="M745 10 H984 Q1010 12 1000 44 L988 92 Q980 116 952 116 H650 Q722 92 745 10 Z" fill="var(--white)"/>
  </svg>
  <div class="brand"><span class="dot"></span>ByteHarbor</div>
  <div class="txt headline" style="top:10px">IT Support and Managed Services</div>
  <div class="txt headline" style="top:47px">IT support you can rely on</div>
  <div class="txt offer">Free remote monitoring and alerting*</div>
  <div class="txt blurb">Our customers are attracted<br>by our exceptional level of<br>customer service and trust us in<br>providing them with&nbsp; support and<br>advice over a ong term relationship.</div>
  <div class="txt terms">*conditions apply</div>
</section>

<section class="banner rectangle" aria-label="Medium rectangle banner">
  <svg class="bg" width="612" height="510" viewBox="0 0 612 510">
    <defs>
      <linearGradient id="mrBlue" x1="0" y1="0" x2="0" y2="1">
        <stop offset="0" stop-color="var(--cyan)"/>
        <stop offset=".5" stop-color="var(--cyan)"/>
        <stop offset=".75" stop-color="var(--cyan-deep)"/>
        <stop offset="1" stop-color="var(--navy-dark)"/>
      </linearGradient>
    </defs>
    <path d="M0 0 H612 V232 C520 336 400 384 300 378 C180 372 70 322 0 274 Z" fill="var(--cyan-deep)"/>
    <path d="M0 0 H612 V226 C520 318 410 352 300 350 C180 348 70 300 0 220 Z" fill="url(#mrBlue)"/>
    <circle cx="548" cy="60" r="124" fill="var(--white)"/>
  </svg>
  <div class="brand"><span class="dot"></span>ByteHarbor</div>
  <div class="txt headline">IT Support and<br>Managed Services</div>
  <div class="txt subline">IT support you can rely on</div>
  <div class="txt offer">Free remote monitoring<br>&nbsp;&nbsp;&nbsp;&nbsp;&nbsp;&nbsp;and alerting*</div>
  <div class="txt blurb">Our customers are attracted by our exceptional level<br>of customer service and trust us in providing them with<br>support&nbsp; and advice over a ong term relationship.</div>
  <div class="txt terms">*conditions apply</div>
</section>

<section class="banner skyscraper" aria-label="Wide skyscraper banner">
  <svg class="bg" width="226" height="852" viewBox="0 0 226 852">
    <defs>
      <linearGradient id="skBlue" x1="0" y1="0" x2="0" y2="1">
        <stop offset="0" stop-color="var(--cyan)"/>
        <stop offset=".55" stop-color="var(--cyan)"/>
        <stop offset=".8" stop-color="var(--cyan-deep)"/>
        <stop offset="1" stop-color="var(--navy-dark)"/>
      </linearGradient>
    </defs>
    <path d="M0 76 Q113 176 226 76 V636 Q113 728 0 648 Z" fill="var(--cyan-deep)"/>
    <path d="M0 76 Q113 176 226 76 V626 Q113 700 0 632 Z" fill="url(#skBlue)"/>
  </svg>
  <div class="brand"><span class="dot"></span>ByteHarbor</div>
  <div class="txt headline">IT Support<br>and<br>Managed<br>Services</div>
  <div class="txt subline">IT support<br>you can<br>rely on</div>
  <div class="txt offer">Free remote<br>monitoring<br>and alerting*</div>
  <div class="txt blurb">Our customers are attracted<br>by our exceptional level<br>of customer service and<br>trust us in providing them<br>with support&nbsp; and advice<br>over a ong term relationship.</div>
  <div class="txt terms">*conditions apply</div>
</section>

</body>
</html>
```